Creative Web Designer: Refresh & Elevate our Beach Lifestyle Brand with a Joyful, Elegant Red...

Corallune (corallune.gr), a vibrant Greek brand celebrated for its high-quality beachwear and accessories, is embarking on an exciting phase as we enter our third year. Renowned for our stylish flip flops, beach towels, and caps, we are thrilled to announce the expansion of our product line with innovative beach essentials and a fresh palette for our existing collection.
As we continue to grow and evolve, we are in search of a talented and imaginative web designer who can capture the essence of Corallune and translate it into a digital experience. Our ideal candidate will craft a website that mirrors the happiness and relaxation of a day at the beach, while also embodying the sophistication and elegance that our brand represents.
Your Mission:
Design a Website That Reflects Our Brand Identity: Create a website that is visually stunning, easy to navigate, and showcases our products in a way that feels both refreshing and luxurious.
Incorporate New Product Lines and Colors: Seamlessly integrate our new beach products and color schemes, ensuring the website remains cohesive and on-brand.
User Experience is Key: Design a user-friendly interface that ensures a seamless shopping experience for our customers, with intuitive navigation and a mobile-responsive design.
Embrace Creativity While Staying Elegant: We want our website to be a reflection of the joy and elegance that our products bring to our customers. Your design should be innovative, incorporating modern web design trends that align with our brand's aesthetic.
What We're Looking For:
A portfolio that demonstrates experience in creating visually appealing and user-friendly e-commerce websites.
Strong understanding of branding and the ability to translate a brand's essence into a digital format.
Proficiency in the latest web design software and technologies.
Excellent communication skills and the ability to work collaboratively with our team to bring our vision to life.
This is a fantastic opportunity for a web designer who loves the beach lifestyle and is passionate about creating beautiful, effective websites. If you're ready to dive into a project that will challenge and excite you, while making a significant impact on our growing brand, we would love to hear from you.
Regarding the products, on the website (corallune.gr) you will the flips flops and on the attached powerpoint all the accessories for this summer. Please use the images to craft your designs.
Join us in making Corallune the go-to brand for beach enthusiasts everywhere. Apply now to start the conversation and share your vision for our new website 😊🩴☀️⛱️
p.s. we didn;t mention the pages to be designed. Its 4 pages in all,
homepage, product category page, singleproduct page and contact us page

```html
<!DOCTYPE html>
<html lang="en">
<head>
<meta charset="utf-8">
<title>Corallune — Summerwear</title>
<link href="https://fonts.googleapis.com/css2?family=Libre+Caslon+Display&family=Poppins:wght@300;400;500;600;700&display=swap" rel="stylesheet">
<style>
:root{
  --navy:#27398a;
  --deep:#133f86;
  --green:#7fae8c;
  --yellow:#e6b415;
  --grey:#9c9c9c;
  --ink:#2b2b2b;
  --muted:#8a8a8a;
  --cream:#f4f2ea;
  --line:#ececec;
  --white:#ffffff;
}
*{box-sizing:border-box;margin:0;padding:0}
html,body{width:1200px;height:4777px;overflow:hidden;background:#fff}
body{font-family:"Poppins",sans-serif;color:var(--ink);position:relative}
.serif{font-family:"Libre Caslon Display",serif;font-weight:400}
section,header,nav,footer,.topbar{position:relative;width:1200px;overflow:hidden}
.abs{position:absolute}
.photo{position:absolute;display:block}
.pill{display:inline-flex;align-items:center;justify-content:center;border-radius:20px;font-weight:600;white-space:nowrap}

/* top bar */
.topbar{height:21px;background:var(--green);color:#fff;font-size:9px;display:flex;align-items:center;justify-content:center;gap:4px}
.topbar b{background:#fff;color:var(--green);padding:0 5px;border-radius:3px;font-weight:600}

/* header */
header{height:67px;background:#fff}
.brand{position:absolute;left:97px;top:14px;color:var(--navy)}
.brand .name{font-size:26px;font-weight:700;line-height:26px;letter-spacing:.5px}
.brand .tag{font-size:7px;letter-spacing:6px;margin-top:3px;font-weight:500}
.search{position:absolute;left:599px;top:22px;width:218px;height:26px;border-radius:14px;background:#f3f3f3;font-size:9px;color:#aaa;padding:7px 14px}
.search i{position:absolute;right:3px;top:3px;width:20px;height:20px;border-radius:50%;background:var(--navy)}
.hicon{position:absolute;top:18px;width:50px;text-align:center;font-size:8px;color:var(--muted)}
.hicon svg{display:block;margin:0 auto 3px}
.cart{position:absolute;left:1007px;top:22px;width:93px;height:26px;border:1px solid #ccc;border-radius:14px;font-size:9px;display:flex;align-items:center;gap:6px;padding-left:14px;color:#555}

/* nav */
nav{height:32px;border-top:1px solid var(--line);border-bottom:1px solid var(--line);display:flex;align-items:center;justify-content:center;gap:42px;font-size:10px;font-weight:500;color:var(--navy)}
nav .home{background:var(--yellow);color:#fff;padding:8px 14px;border-radius:0 0 4px 4px;margin-top:-2px}

/* hero */
.hero{height:498px}
.hero .photo{inset:0;background:linear-gradient(160deg,#5c7384 0%,#8aa0a5 35%,#b9a77a 65%,#d8c9a6 100%)}
.hero .badge{position:absolute;left:180px;top:100px;width:84px;height:84px;border-radius:50%;background:var(--green);color:#fff;font-size:11px;display:flex;align-items:center;justify-content:center;letter-spacing:.5px}
.hero h1{position:absolute;left:198px;top:162px;font-size:60px;color:#fff;line-height:1}
.hero p{position:absolute;left:198px;top:237px;font-size:15px;color:#fff}
.hero .btn{position:absolute;left:198px;top:275px;width:122px;height:32px;background:#fff;color:var(--navy);font-size:11px}
.hero .edge{position:absolute;left:0;bottom:0;width:1200px;height:60px}

/* categories */
.cats{height:507px;background:linear-gradient(180deg,#f3f7fa 0%,#eef1f1 45%,#e4dccd 75%,#d8cdb8 100%)}
.sec-title{font-size:33px;color:var(--navy)}
.cats .sec-title{position:absolute;top:92px;width:100%;text-align:center}
.cat{position:absolute;top:166px;width:176px;text-align:center;font-size:12px;color:var(--ink);font-weight:500}
.cat .photo{position:relative;width:176px;height:176px;margin-bottom:18px}
.cats .arrow{position:absolute;top:244px;color:#999;font-size:16px}
.cats .btn{position:absolute;left:524px;top:402px;width:152px;height:34px;background:var(--yellow);color:#fff;font-size:10px}

/* product lists */
.plist .sec-title{position:absolute;left:200px}
.navarrows{position:absolute;display:flex;gap:8px;z-index:2}
.navarrows span{width:30px;height:30px;border-radius:50%;border:1.5px solid var(--yellow);background:#fff;color:var(--yellow);font-size:13px;display:flex;align-items:center;justify-content:center}
.card{position:absolute;width:238px;height:332px;background:#fff;border:1px solid #f0f0f0;box-shadow:0 4px 14px rgba(0,0,0,.05);padding:12px}
.card .photo{position:relative;width:212px;height:190px;background:#f5f5f5}
.card .cat-l{font-size:8px;color:var(--green);margin-top:16px}
.card .nm{font-size:12px;font-weight:500;margin-top:4px}
.card .pr{font-size:11px;color:var(--muted);margin-top:2px}
.card .btn{margin-top:16px;width:104px;height:26px;background:var(--grey);color:#fff;font-size:9px}
.card .btn.on{background:var(--navy)}
.card .new{position:absolute;left:12px;top:12px;background:#2f7ec9;color:#fff;font-size:8px;padding:2px 8px;border-radius:3px;z-index:1}
.leaf{position:absolute;border-radius:50% 10% 50% 10%;background:radial-gradient(circle at 60% 40%,#9fc49d,#6e9c72 70%,transparent 72%);opacity:.75;z-index:0}

.featured{height:564px}
.popular{height:558px}

/* promo */
.gap{height:41px}
.promo{height:334px;background:var(--navy)}
.promo .season{position:absolute;left:198px;top:70px;font-size:12px;color:#fff}
.promo .rule{position:absolute;left:0;top:128px;width:150px;height:1px;background:rgba(255,255,255,.6)}
.promo h2{position:absolute;left:198px;top:98px;font-size:40px;color:#fff;line-height:46px;width:345px}
.promo h2 em{font-style:normal;color:var(--yellow)}
.promo h2 small{font-size:22px;color:var(--yellow)}
.promo .btn{position:absolute;left:198px;top:224px;width:170px;height:30px;background:var(--yellow);color:#fff;font-size:9px}
.promo .ghost{position:absolute;left:0;top:268px;font-size:64px;font-weight:700;color:rgba(255,255,255,.1);letter-spacing:2px;line-height:1}
.promo .tag{position:absolute;left:590px;top:28px;font-size:15px;color:var(--navy);text-align:center;line-height:18px}

/* newsletter */
.news{height:334px}
.news .photo{inset:0;background:linear-gradient(180deg,#bfe0ef 0%,#d9eef4 30%,#7fcfd2 48%,#f1eadb 62%,#f6f1e6 100%)}
.news h2{position:absolute;left:268px;top:100px;font-size:40px;color:var(--navy)}
.news p{position:absolute;left:268px;top:158px;font-size:10px;color:#555}
.news .field{position:absolute;left:268px;top:188px;width:362px;height:30px;background:#fff;border-radius:16px;font-size:9px;color:#aaa;padding:9px 16px}
.news .btn{position:absolute;left:268px;top:234px;width:122px;height:30px;background:var(--navy);color:#fff;font-size:9px}
.news .mark{position:absolute;left:712px;top:232px;color:rgba(39,57,138,.55);text-align:center}
.news .mark .name{font-size:60px;font-weight:700;line-height:60px}
.news .mark .tag{font-size:12px;letter-spacing:16px;margin-top:2px}

/* about */
.about{height:634px}
.about .box{position:absolute;left:482px;top:108px;width:498px;height:518px;background:var(--cream)}
.about .pic{left:200px;top:97px;width:387px;height:391px;background:linear-gradient(180deg,#7fb6d8 0%,#a7cde0 45%,#3e7fae 58%,#d9c7a4 75%,#cdb78f 100%)}
.about .script{position:absolute;left:649px;top:118px;width:260px;height:34px;background:linear-gradient(90deg,rgba(127,174,140,.35),rgba(127,174,140,.1))}
.about h3{position:absolute;left:649px;top:166px;font-size:27px;color:var(--navy);line-height:34px;width:300px}
.about p{position:absolute;left:649px;width:300px;font-size:9px;line-height:16px;color:#666}
.about .btn{position:absolute;left:649px;top:448px;width:122px;height:30px;background:var(--green);color:#fff;font-size:9px}

/* features */
.feats{height:154px;background:var(--deep);display:flex;align-items:center}
.feat{flex:1;text-align:center;color:#fff;font-size:10px}
.feats .divider{width:1px;height:96px;background:rgba(255,255,255,.35)}
.feat svg{display:block;margin:0 auto 12px}
.feats .wrap{width:816px;margin:0 auto;display:flex;align-items:center}

/* instagram */
.insta{height:588px}
.insta h2{position:absolute;top:76px;width:100%;text-align:center;font-size:32px;color:var(--navy);display:flex;align-items:center;justify-content:center;gap:12px}
.insta h2 i{width:22px;height:22px;border:2.5px solid var(--navy);border-radius:50%}
.insta .btn{position:absolute;left:520px;top:478px;width:160px;height:32px;background:var(--green);color:#fff;font-size:9px}

/* footer */
footer{height:403px;background:linear-gradient(180deg,#2f4f98 0%,#2a5ba6 55%,#2e6fb4 100%);color:#fff}
footer .brand{left:97px;top:80px;color:#fff}
footer .brand .name{font-size:34px;line-height:34px}
footer .brand .tag{font-size:8px;letter-spacing:9px}
footer h4{font-size:15px;margin-bottom:14px}
.fcol{position:absolute;top:78px;font-size:9px;line-height:20px}
.fcol .row{display:flex;align-items:flex-start;gap:8px}
.fcol .row svg{margin-top:5px;flex:none}
.social{display:flex;gap:12px;margin-top:12px}
.social span{width:26px;height:26px;border-radius:50%;background:var(--deep);border:1px solid rgba(255,255,255,.5)}
.social span.y{background:var(--yellow);border:0}
footer .copy{position:absolute;left:97px;top:352px;font-size:8px}
footer .copy b{color:var(--yellow);font-weight:600}
.pay{position:absolute;left:690px;top:344px;display:flex;gap:14px}
.pay span{width:40px;height:22px;border-radius:3px;background:rgba(255,255,255,.85)}
.totop{position:absolute;left:1142px;top:344px}
</style>
</head>
<body>

<div class="topbar">Free Domestic Shipping on Orders Above €35 <b>Shop Now</b></div>

<header>
  <div class="brand"><div class="name">Corallune</div><div class="tag">SUMMERWEAR</div></div>
  <div class="search">Search products…<i></i></div>
  <div class="hicon" style="left:852px"><svg width="16" height="16" viewBox="0 0 16 16" fill="none" stroke="#27398a" stroke-width="1.4"><circle cx="8" cy="5" r="3"/><path d="M2 15c0-3.5 2.7-5.5 6-5.5s6 2 6 5.5"/></svg>Account</div>
  <div class="hicon" style="left:928px"><svg width="16" height="16" viewBox="0 0 16 16" fill="none" stroke="#27398a" stroke-width="1.4"><path d="M8 14S2 10 2 5.8A3.2 3.2 0 0 1 8 4a3.2 3.2 0 0 1 6 1.8C14 10 8 14 8 14z"/></svg>Wish list</div>
  <div class="cart"><svg width="12" height="12" viewBox="0 0 12 12" fill="none" stroke="#27398a" stroke-width="1.3"><path d="M2 4h8l-1 7H3z"/><path d="M4 4V3a2 2 0 0 1 4 0v1"/></svg>€ 0.00</div>
</header>

<nav>
  <span class="home">Home</span><span>Flip Flops</span><span>Pouches</span><span>Bags ⌄</span><span>Hats ⌄</span><span>Caps</span><span>Scrunchies</span><span>Towels</span><span>About Us</span><span>Contact Us</span>
</nav>

<section class="hero">
  <div class="photo" role="img" aria-label="Couple wearing bucket hats leaning on a vintage van by the sea"></div>
  <div class="badge">EXCLUSIVE</div>
  <h1 class="serif">Dune bucket</h1>
  <p>Wide visor for full coverage from the sun.</p>
  <span class="pill btn">Shop Now!</span>
  <svg class="edge" viewBox="0 0 1200 60" preserveAspectRatio="none"><path d="M0 38 Q150 22 300 36 T600 32 T900 38 T1200 30 V60 H0Z" fill="#f3f7fa"/></svg>
</section>

<section class="cats">
  <h2 class="serif sec-title">Shop by categories</h2>
  <span class="arrow" style="left:48px">‹</span><span class="arrow" style="left:1144px">›</span>
  <div class="cat" style="left:100px"><span class="photo" role="img" aria-label="Blue flip flops on sand" style="background:linear-gradient(135deg,#c9b595,#8fa6cf)"></span>Flip Flops</div>
  <div class="cat" style="left:306px"><span class="photo" role="img" aria-label="Printed pouch with crab pattern" style="background:linear-gradient(135deg,#f0e7d7,#e9a57f)"></span>Pouches</div>
  <div class="cat" style="left:513px"><span class="photo" role="img" aria-label="White tote bag on coral background" style="background:linear-gradient(135deg,#ee6f67,#f4f1ec)"></span>Bags</div>
  <div class="cat" style="left:720px"><span class="photo" role="img" aria-label="Patterned bucket hat" style="background:linear-gradient(135deg,#a8c5d6,#e07f5d)"></span>Hats</div>
  <div class="cat" style="left:924px"><span class="photo" role="img" aria-label="Printed cap" style="background:linear-gradient(135deg,#f0e6dd,#d89a74 60%,#7fae8c)"></span>Caps</div>
  <span class="pill btn">View All Categories</span>
</section>

<section class="featured plist">
  <div class="leaf" role="img" aria-label="Palm leaves" style="left:1070px;top:-20px;width:150px;height:190px"></div>
  <h2 class="serif sec-title" style="top:70px">Featured products</h2>
  <div class="navarrows" style="left:1030px;top:74px;transform:translateX(-100%)"><span>←</span><span>→</span></div>
  <div class="photo" role="img" aria-label="Couple in summer clothes on a seaside boardwalk" style="left:0;top:143px;width:330px;height:387px;background:linear-gradient(180deg,#8fb8d6,#d7c9b1 60%,#a78a67)"></div>
  <div class="card" style="left:359px;top:175px"><span class="new">New</span><span class="photo" role="img" aria-label="Yellow flip flops"></span><div class="cat-l">Flip Flops</div><div class="nm">Daybreak Flip Flops</div><div class="pr">€ 19.90</div><span class="pill btn">Shop Now!</span></div>
  <div class="card" style="left:615px;top:175px"><span class="photo" role="img" aria-label="Black tote bag"></span><div class="cat-l">Bags</div><div class="nm">Tote Bag</div><div class="pr">€ 16.90</div><span class="pill btn on">Shop Now!</span></div>
  <div class="card" style="left:869px;top:175px"><span class="photo" role="img" aria-label="Sand coloured bucket hat"></span><div class="cat-l">Hats</div><div class="nm">Dune Bucket</div><div class="pr">€ 17.90</div><span class="pill btn">Shop Now!</span></div>
</section>

<div class="gap"></div>

<section class="promo">
  <svg class="abs" style="left:0;top:0" width="1200" height="334" viewBox="0 0 1200 334">
    <polygon points="560,0 860,0 760,334 510,334" fill="#e9c968"/>
    <polygon points="600,80 860,0 900,334 540,334" fill="#5f8fb5" role="img" aria-label="Legs with flip flops over the sea"/>
    <polygon points="900,0 1200,0 1200,334 830,334" fill="#6f9cc4" role="img" aria-label="Woman in red cap facing the sea"/>
  </svg>
  <span class="rule"></span>
  <div class="season">Spring — Summer 2024</div>
  <h2 class="serif"><em>10</em><small>%</small> Off your first order</h2>
  <span class="pill btn">Shop New Collections</span>
  <div class="ghost">Corallune</div>
  <div class="tag serif">100%<br>Natural Rubber</div>
</section>

<section class="popular plist">
  <div class="leaf" role="img" aria-label="Palm leaves" style="left:-30px;top:10px;width:150px;height:180px"></div>
  <h2 class="serif sec-title" style="top:66px">Most popular products</h2>
  <div class="navarrows" style="left:1064px;top:70px;transform:translateX(-100%)"><span>←</span><span>→</span></div>
  <div class="card" style="left:109px;top:177px"><span class="photo" role="img" aria-label="Printed beach towel"></span><div class="cat-l">Towels</div><div class="nm">Pebble Towel</div><div class="pr">€ 24.90</div><span class="pill btn">Shop Now!</span></div>
  <div class="card" style="left:364px;top:177px"><span class="photo" role="img" aria-label="Maroon cap"></span><div class="cat-l">Caps</div><div class="nm">Ember Cap</div><div class="pr">€ 15.90</div><span class="pill btn">Shop Now!</span></div>
  <div class="card" style="left:620px;top:177px"><span class="photo" role="img" aria-label="Black bucket hat"></span><div class="cat-l">Hats</div><div class="nm">Nightfall Bucket</div><div class="pr">€ 17.90</div><span class="pill btn">Shop Now!</span></div>
  <div class="photo" role="img" aria-label="Beach chair with tote bag and flip flops on the sand" style="left:867px;top:138px;width:333px;height:389px;background:linear-gradient(180deg,#a9c9e6,#cfe0ea 40%,#7fb0c9 52%,#e3d3b7 70%,#d8c3a0)"></div>
</section>

<div class="gap"></div>

<section class="news">
  <div class="photo" role="img" aria-label="Tropical beach with turquoise water and pier"></div>
  <h2 class="serif">Stay in touch</h2>
  <p>Joining our mailing list, and receive some of the best deals possible.</p>
  <div class="field">Enter your email…</div>
  <span class="pill btn">SUBSCRIBE</span>
  <div class="mark"><div class="name">Corallune</div><div class="tag">SUMMERWEAR</div></div>
</section>

<section class="about">
  <div class="leaf" role="img" aria-label="Palm leaves" style="left:1050px;top:0;width:160px;height:160px"></div>
  <div class="leaf" role="img" aria-label="Palm leaves" style="left:-40px;top:380px;width:160px;height:220px"></div>
  <div class="box"></div>
  <div class="photo pic" role="img" aria-label="Two people posing playfully on a beach"></div>
  <div class="script" role="img" aria-label="Hand lettered line: Corallune was born in Greece"></div>
  <h3 class="serif">Our Greek and sustainable answer for summer flip flops.</h3>
  <p style="top:300px">Greece means summer. Our country has blue waters, clear blue skies, numerous islands, a burning sun that warms us, and countless beautiful sandy beaches.</p>
  <p style="top:370px">Visitors arrive from all over the world to get a taste of the Greek summer as it is undoubtedly one of the best summer experiences one could have …</p>
  <span class="pill btn">Discover More</span>
</section>

<section class="feats">
  <div class="wrap">
    <div class="feat"><svg width="38" height="40" viewBox="0 0 38 40" fill="none" stroke="#e6b415" stroke-width="2"><circle cx="19" cy="15" r="12"/><path d="M13 15l4 4 8-8"/><path d="M12 25l-4 12 7-3 4 5M26 25l4 12-7-3-4 5"/></svg>100% Guaranteed</div>
    <span class="divider"></span>
    <div class="feat"><svg width="40" height="40" viewBox="0 0 40 40" fill="none" stroke="#ffffff" stroke-width="2"><rect x="6" y="6" width="26" height="26" rx="2"/><path d="M15 6v10l4-3 4 3V6"/><circle cx="31" cy="31" r="6" stroke="#e6b415"/><path d="M28 31h6M31 28l3 3-3 3" stroke="#e6b415"/></svg>Free Shipping &amp; Returns</div>
    <span class="divider"></span>
    <div class="feat"><svg width="40" height="40" viewBox="0 0 40 40" fill="none" stroke="#7fae8c" stroke-width="2"><path d="M8 22v-4a12 12 0 0 1 24 0v4"/><rect x="5" y="21" width="6" height="10" rx="2"/><rect x="29" y="21" width="6" height="10" rx="2"/><path d="M32 31c0 4-4 5-9 5"/></svg>Customer Support</div>
  </div>
</section>

<section class="insta">
  <div class="leaf" role="img" aria-label="Palm leaves" style="left:1050px;top:340px;width:160px;height:220px"></div>
  <h2 class="serif"><i></i>corallune.gr</h2>
  <div class="photo" role="img" aria-label="Woman in yellow bucket hat" style="left:200px;top:143px;width:316px;height:301px;background:linear-gradient(180deg,#d9b35a,#e8dcc8 60%,#efe8de)"></div>
  <div class="photo" role="img" aria-label="Bag detail" style="left:522px;top:143px;width:150px;height:143px;background:linear-gradient(135deg,#b67a63,#3b3a44)"></div>
  <div class="photo" role="img" aria-label="Sandals in a van" style="left:686px;top:143px;width:150px;height:143px;background:linear-gradient(135deg,#d8b391,#7d6a58)"></div>
  <div class="photo" role="img" aria-label="Beach bag on grass" style="left:848px;top:143px;width:150px;height:143px;background:linear-gradient(135deg,#7fae6a,#c9a87c)"></div>
  <div class="photo" role="img" aria-label="Friends by a van" style="left:522px;top:301px;width:150px;height:143px;background:linear-gradient(135deg,#7fa0a7,#d4c2a4)"></div>
  <div class="photo" role="img" aria-label="Woman in red cap by the sea" style="left:686px;top:301px;width:150px;height:143px;background:linear-gradient(135deg,#5d8fc0,#b04a45)"></div>
  <div class="photo" role="img" aria-label="Man in black bucket hat" style="left:848px;top:301px;width:150px;height:143px;background:linear-gradient(135deg,#6c9e66,#2e3038)"></div>
  <span class="pill btn">Follow Us On Instagram</span>
</section>

<footer>
  <div class="brand"><div class="name">Corallune</div><div class="tag">SUMMERWEAR</div></div>
  <div class="fcol" style="left:406px">
    <h4 class="serif">Contact us</h4>
    <div class="row"><svg width="10" height="10" viewBox="0 0 10 10" fill="#e6b415"><path d="M2 0l2 2-1 2 3 3 2-1 2 2-2 2C4 10 0 6 0 2z"/></svg><span style="font-size:11px">+30 210 555 0142</span></div>
    <div class="row"><svg width="10" height="8" viewBox="0 0 10 8" fill="none" stroke="#e6b415"><rect x=".5" y=".5" width="9" height="7"/><path d="M.5 .5l4.5 4 4.5-4"/></svg>info@corallune.gr</div>
    <div class="row"><svg width="9" height="11" viewBox="0 0 9 11" fill="#e6b415"><path d="M4.5 0A4.5 4.5 0 0 0 0 4.5C0 8 4.5 11 4.5 11S9 8 9 4.5A4.5 4.5 0 0 0 4.5 0zm0 6a1.5 1.5 0 1 1 0-3 1.5 1.5 0 0 1 0 3z"/></svg><span style="line-height:16px"><b style="color:#e6b415;font-weight:500">Corallune</b><br>12 Aegeou Str., Kallithea, 176 71,<br>Attica, GR</span></div>
    <div class="social"><span></span><span class="y"></span></div>
  </div>
  <div class="fcol" style="left:680px">
    <h4 class="serif">Quick links</h4>
    Home<br>About us<br>Shipping<br>Terms of Use<br>Privacy Policy<br>Refund Policy<br>Download our Catalogue<br>Contact Us
  </div>
  <div class="fcol" style="left:887px">
    <h4 class="serif">Categories</h4>
    Flip Flops<br>Pouches<br>Bags<br>Hats<br>Caps<br>Scrunchies<br>Towels
  </div>
  <div class="copy">© 2024 <b>CORALLUNE</b>. All Right Reserved</div>
  <div class="pay"><span></span><span></span><span></span><span></span><span></span><span></span></div>
  <svg class="totop" width="16" height="16" viewBox="0 0 16 16" fill="#e6b415"><path d="M8 2l6 12H2z"/></svg>
</footer>

</body>
</html>
```